Product Setup Instructional Infographic/flyer

Converting product instructions into an infographic. Would prefer that the instructions fit on a 4x6 card, front and back, but a slightly larger size is acceptable as well.

Logo Text

Harbor Crest (Rebranding just as Harbor Crest, instead of Harbor Crest Casks)

Font styles to use
Decorative

Colors

Designer to choose colors to be used in the design.

Requirements
Must have
• NA
Nice to have
• NA
Should not have
• NA

```html
<!DOCTYPE html>
<html lang="en">
<head>
<meta charset="UTF-8">
<title>Barrel Curing Steps</title>
<link href="https://fonts.googleapis.com/css2?family=Cinzel+Decorative:wght@400;700&family=Roboto+Condensed:wght@400&display=swap" rel="stylesheet">
<style>
  :root {
    --parchment-light: #efe6d2;
    --parchment: #e3d6bb;
    --parchment-dark: #c9b996;
    --card: #f2eddc;
    --card-edge: #e2dbc4;
    --wood-light: #d9a467;
    --wood: #b97d44;
    --wood-dark: #8a5628;
    --ink: #7a3f12;
    --body-ink: #6b3a17;
  }
  * { margin: 0; padding: 0; box-sizing: border-box; }
  html, body { width: 1200px; height: 799px; overflow: hidden; }
  body {
    position: relative;
    background: radial-gradient(ellipse at 50% 45%, var(--parchment-light) 0%, var(--parchment) 55%, var(--parchment-dark) 100%);
    font-family: "Roboto Condensed", "Arial Narrow", sans-serif;
  }
  .board {
    position: absolute;
    width: 196px;
    height: 300px;
    border-radius: 14px;
    background:
      repeating-linear-gradient(90deg, rgba(120,70,30,0.18) 0 2px, transparent 2px 11px, rgba(255,230,190,0.12) 11px 13px, transparent 13px 23px),
      linear-gradient(90deg, var(--wood-dark), var(--wood) 12%, var(--wood-light) 50%, var(--wood) 88%, var(--wood-dark));
    box-shadow: 0 3px 6px rgba(60,35,10,0.3);
  }
  .card {
    position: absolute;
    width: 234px;
    height: 258px;
    filter: drop-shadow(0 3px 5px rgba(60,35,10,0.3));
  }
  .card-shape { position: absolute; inset: 0; }
  .card-text {
    position: absolute;
    left: 13px;
    right: 12px;
    font-size: 11.4px;
    line-height: 13.6px;
    color: var(--body-ink);
    text-align: justify;
    text-indent: 1.6em;
  }
  .card-top .card-text { top: 162px; }
  .card-bottom .card-text { top: 12px; }
  .step-label {
    position: absolute;
    font-family: "Cinzel Decorative", serif;
    color: var(--ink);
    line-height: 1;
    white-space: nowrap;
  }
  .step-num { font-size: 86px; }
  .step-word { font-size: 40px; }
  .card-top .step-num { top: 2px; left: 112px; }
  .card-top .step-word { top: 84px; left: 112px; }
  .card-bottom .step-num { top: 126px; left: 116px; }
  .card-bottom .step-word { top: 206px; left: 114px; }
  .tip-small { font-size: 16px; top: 152px; left: 106px; }
  .tip-big { font-size: 56px; top: 180px; left: 114px; }
</style>
</head>
<body>

<svg width="0" height="0" style="position:absolute">
  <defs>
    <linearGradient id="woodFill" x1="0" y1="0" x2="1" y2="0">
      <stop offset="0" stop-color="#9a6131"/>
      <stop offset="0.5" stop-color="#cf9a5e"/>
      <stop offset="1" stop-color="#9a6131"/>
    </linearGradient>
  </defs>
</svg>

<div class="board" style="left:62px; top:68px;"></div>
<div class="board" style="left:355px; top:68px;"></div>
<div class="board" style="left:647px; top:68px;"></div>
<div class="board" style="left:938px; top:68px;"></div>

<div class="board" style="left:62px; top:414px;"></div>
<div class="board" style="left:355px; top:414px;"></div>
<div class="board" style="left:647px; top:414px;"></div>
<div class="board" style="left:938px; top:414px;"></div>

<div class="card card-top" style="left:42px; top:114px;">
  <svg class="card-shape" viewBox="0 0 234 258" width="234" height="258">
    <rect x="0.5" y="0.5" width="233" height="257" rx="12" fill="var(--card)" stroke="var(--card-edge)"/>
    <path role="img" aria-label="Barrel illustration" d="M51,0 V52.8 A42 42 0 1 0 81 52.8 V0 Z" fill="url(#woodFill)"/>
  </svg>
  <div class="step-label step-num">01</div>
  <div class="step-label step-word">STEP</div>
  <p class="card-text">Rinse and soak the spigot (wooden faucet) and the plug (or bung) in water for about half an hour.</p>
</div>

<div class="card card-top" style="left:335px; top:114px;">
  <svg class="card-shape" viewBox="0 0 234 258" width="234" height="258">
    <rect x="0.5" y="0.5" width="233" height="257" rx="12" fill="var(--card)" stroke="var(--card-edge)"/>
    <path role="img" aria-label="Barrel with spigot illustration" d="M51,0 V52.8 A42 42 0 1 0 81 52.8 V0 Z" fill="url(#woodFill)"/>
  </svg>
  <div class="step-label step-num">02</div>
  <div class="step-label step-word">STEP</div>
  <p class="card-text" style="top:136px;">While waiting, fill the barrel with water until it is half-full. Use your thumb to plug the holes, give it a good shake to get rid of wood chips and debris that might be trapped inside. Let the water out. You may repeat this process three to five times until you satisfied the barrel is thoroughly clean.</p>
</div>

<div class="card card-top" style="left:627px; top:114px;">
  <svg class="card-shape" viewBox="0 0 234 258" width="234" height="258">
    <rect x="0.5" y="0.5" width="233" height="257" rx="12" fill="var(--card)" stroke="var(--card-edge)"/>
    <path role="img" aria-label="Barrel illustration" d="M51,0 V52.8 A42 42 0 1 0 81 52.8 V0 Z" fill="url(#woodFill)"/>
  </svg>
  <div class="step-label step-num">03</div>
  <div class="step-label step-word">STEP</div>
  <p class="card-text" style="top:150px;">Plug the barrel with the spigot. You may tighten it securely with your hand. We advise not to use a hammer as it may crack the wood.</p>
</div>

<div class="card card-top" style="left:918px; top:114px;">
  <svg class="card-shape" viewBox="0 0 234 258" width="234" height="258">
    <rect x="0.5" y="0.5" width="233" height="257" rx="12" fill="var(--card)" stroke="var(--card-edge)"/>
    <path role="img" aria-label="Barrel illustration" d="M51,0 V52.8 A42 42 0 1 0 81 52.8 V0 Z" fill="url(#woodFill)"/>
  </svg>
  <div class="step-label step-num">04</div>
  <div class="step-label step-word">STEP</div>
  <p class="card-text" style="top:150px;">Place the barrel in a sink, tub, or any place that is OK to get wet.</p>
</div>

<div class="card card-bottom" style="left:42px; top:414px;">
  <svg class="card-shape" viewBox="0 0 234 258" width="234" height="258">
    <rect x="0.5" y="0.5" width="233" height="257" rx="12" fill="var(--card)" stroke="var(--card-edge)"/>
    <path role="img" aria-label="Barrel illustration" d="M51,258 V213.2 A42 42 0 1 1 81 213.2 V258 Z" fill="url(#woodFill)"/>
  </svg>
  <p class="card-text">Using a funnel, fill the barrel with hot water until it is full. Leave the top hole open. Your barrel might leak, and that's OK. It is not watertight yet and this process will make the wood expand to seal the gaps.</p>
  <div class="step-label step-num">05</div>
  <div class="step-label step-word">STEP</div>
</div>

<div class="card card-bottom" style="left:335px; top:414px;">
  <svg class="card-shape" viewBox="0 0 234 258" width="234" height="258">
    <rect x="0.5" y="0.5" width="233" height="257" rx="12" fill="var(--card)" stroke="var(--card-edge)"/>
    <path role="img" aria-label="Barrel on its side illustration" d="M51,258 V213.2 A42 42 0 1 1 81 213.2 V258 Z" fill="url(#woodFill)"/>
  </svg>
  <p class="card-text">Leave the barrel this way until no more leakages can be seen. This means the wood has expanded and the gaps are sealed. This can take from 30 minutes to an entire week, depending on the size of the barrel.</p>
  <div class="step-label step-num">06</div>
  <div class="step-label step-word">STEP</div>
</div>

<div class="card card-bottom" style="left:627px; top:414px;">
  <svg class="card-shape" viewBox="0 0 234 258" width="234" height="258">
    <rect x="0.5" y="0.5" width="233" height="257" rx="12" fill="var(--card)" stroke="var(--card-edge)"/>
    <path role="img" aria-label="Barrels illustration" d="M51,258 V213.2 A42 42 0 1 1 81 213.2 V258 Z" fill="url(#woodFill)"/>
  </svg>
  <p class="card-text">Drain the barrel and let it air dry for no more than four hours. After 4 hours, it is ready to be filled with any spirits or wine of your choice.</p>
  <div class="step-label step-num">07</div>
  <div class="step-label step-word">STEP</div>
</div>

<div class="card card-bottom" style="left:918px; top:414px;">
  <svg class="card-shape" viewBox="0 0 234 258" width="234" height="258">
    <rect x="0.5" y="0.5" width="233" height="257" rx="12" fill="var(--card)" stroke="var(--card-edge)"/>
    <path role="img" aria-label="Barrel with spigot illustration" d="M51,258 V213.2 A42 42 0 1 1 81 213.2 V258 Z" fill="url(#woodFill)"/>
  </svg>
  <p class="card-text" style="font-size:11px; line-height:13px;">If you plan on aging different kinds of alcohol using the same barrel, you must cure the barrel again.................. (Step 6) for three to five days. This will allow the barrel to absorb enough water and prevent the next batch of alcohol from being contaminated.</p>
  <div class="step-label tip-small">ADDITIONAL</div>
  <div class="step-label tip-big">TIP</div>
</div>

</body>
</html>
```